https://dorvakel.com

We need a cool technology design for our Managed IT Services company. We are located in Coral Springs Florida. We provide all IT services and support for small to medium sized businesses. We would like to see designs that use our blue and white colors from our website.

```html
<!DOCTYPE html>
<html lang="en">
<head>
<meta charset="utf-8">
<title>Dorvakel Business Card</title>
<link rel="stylesheet" href="https://fonts.googleapis.com/css2?family=Roboto:wght@400;500;700&family=Roboto+Condensed:wght@500;700&display=swap">
<style>
  :root {
    --navy: #0b2c50;
    --paper: #f3f3f3;
    --ink: #4a4a4a;
    --muted: #9a9a9a;
    --mark: #d6d9dd;
    --backdrop: #e7e4df;
    --white: #ffffff;
  }
  * { margin: 0; padding: 0; box-sizing: border-box; }
  html, body {
    width: 1200px; height: 960px; overflow: hidden;
    background: var(--backdrop);
    font-family: "Roboto", Arial, sans-serif;
  }
  .canvas { position: relative; width: 1200px; height: 960px; }
  .card {
    position: absolute; width: 600px; height: 343px;
    background: var(--paper);
    box-shadow: 0 2px 6px rgba(0,0,0,0.18);
  }
  .card--front { left: 314px; top: 113px; }
  .card--back { left: 311px; top: 472px; }

  .brand-name {
    position: absolute; left: 0; right: 0; top: 44px;
    text-align: center;
    font-family: "Roboto", Arial, sans-serif;
    font-weight: 700; font-size: 52px; letter-spacing: -0.5px;
    color: var(--navy); line-height: 1;
  }
  .person-name {
    position: absolute; left: 0; right: 0; top: 155px;
    text-align: center;
    font-family: "Roboto Condensed", Arial, sans-serif;
    font-weight: 700; font-size: 25px; color: var(--navy); line-height: 1;
  }
  .person-role {
    position: absolute; left: 0; right: 0; top: 183px;
    text-align: center;
    font-family: "Roboto Condensed", Arial, sans-serif;
    font-weight: 500; font-size: 16px; color: var(--muted); line-height: 1;
  }
  .contact {
    position: absolute; left: 0; right: 0; top: 212px;
    text-align: center; font-size: 15px; line-height: 19px; color: var(--ink);
  }
  .contact b { font-weight: 700; }
  .address-band {
    position: absolute; left: 0; right: 0; top: 276px; height: 38px;
    background: var(--navy); color: var(--white);
    display: flex; align-items: center; justify-content: center; gap: 8px;
    font-size: 14.5px;
  }
  .pin-icon { width: 12px; height: 16px; }

  .back-mark {
    position: absolute; left: 250px; top: 90px;
    width: 100px; height: 100px; border-radius: 50%;
    background: var(--mark);
  }
  .back-url {
    position: absolute; left: 0; right: 0; top: 284px;
    text-align: center; font-size: 14px; letter-spacing: 0.55em;
    color: var(--ink); padding-left: 0.55em;
  }
</style>
</head>
<body>
<main class="canvas">
  <section class="card card--front">
    <div class="brand-name">DORVAKEL</div>
    <div class="person-name">MAREK OLSEN</div>
    <div class="person-role">CEO/FOUNDER</div>
    <div class="contact">
      <div><b>P:</b> (954) 555-0148 <b>E:</b> marek@dorvakel.com</div>
      <div><b>W:</b> www.dorvakel.com</div>
    </div>
    <div class="address-band">
      <svg class="pin-icon" viewBox="0 0 12 16" aria-hidden="true">
        <path d="M6 0a6 6 0 0 0-6 6c0 4.5 6 10 6 10s6-5.5 6-10a6 6 0 0 0-6-6zm0 8.3A2.3 2.3 0 1 1 6 3.7a2.3 2.3 0 0 1 0 4.6z" fill="#ffffff"/>
      </svg>
      <span>2870 Palmetto Ridge Rd #140 Coral Springs, Florida 33065</span>
    </div>
  </section>

  <section class="card card--back">
    <div class="back-mark"></div>
    <div class="back-url">www.dorvakel.com</div>
  </section>
</main>
</body>
</html>
```